Brightwell Consulting Business Card Design

Business Card Design for Brightwell Consulting. Brightwell Consulting is a boutique consultancy based in Atlanta, GA., that specializes in marketing strategy, organization planning, and leadership development. We provide solutions for small businesses and startups as well as Summit 400 companies.

http://brightwellconsulting.example/

Target Market(s)

We provide solutions for small businesses and startups as well as Summit 400 companies.

Industry/Entity Type

Consulting

Contact Information for Business Card

Two sided business card with priority on contact information, logo, tag line (Inspiration to Dream More, Do More, Become More)

Colors

Designer to choose colors to be used in the design.

Requirements
Must have
• contact information, logo, tag line (Inspiration to Dream More, Do More, Become More)
• Simple no over communication.
Nice to have
• I would like to see different placements of logo and creative use of both sides of the card
Should not have
• Do not put too much information on the card.

```html
<!DOCTYPE html>
<html lang="en">
<head>
<meta charset="utf-8">
<title>Brightwell Consulting Business Card</title>
<link href="https://fonts.googleapis.com/css2?family=Arimo:wght@400&display=swap" rel="stylesheet">
<style>
  :root {
    --page: #ffffff;
    --frame: #1a1a1a;
    --card-dark: #232a33;
    --card-blue: #03b0dc;
    --ink-light: #ffffff;
    --ink-dark: #000000;
  }
  * { margin: 0; padding: 0; box-sizing: border-box; }
  html, body {
    width: 1200px;
    height: 1200px;
    overflow: hidden;
    background: var(--page);
  }
  .canvas {
    position: relative;
    width: 1200px;
    height: 1200px;
    border: 2px solid var(--frame);
    font-family: "Arimo", Arial, sans-serif;
  }
  .card {
    position: absolute;
    left: 64px;
    top: 286px;
    width: 1072px;
    height: 628px;
    background: var(--card-dark);
    border: 1px solid var(--ink-dark);
    overflow: hidden;
  }
  .card-shapes {
    position: absolute;
    inset: 0;
    width: 100%;
    height: 100%;
  }
  .brand-name {
    position: absolute;
    left: 22px;
    top: 22px;
    color: var(--ink-light);
    font-weight: 400;
    line-height: 1;
  }
  .brand-name .word-main {
    display: block;
    font-size: 92px;
    letter-spacing: -1px;
  }
  .brand-name .word-sub {
    display: block;
    margin-top: 18px;
    font-size: 40px;
    letter-spacing: 4px;
  }
  .tagline {
    position: absolute;
    left: 24px;
    top: 204px;
    color: var(--ink-light);
    font-size: 21px;
    letter-spacing: 0.5px;
    white-space: nowrap;
  }
  .holder {
    position: absolute;
    left: 54px;
    top: 490px;
    font-size: 42px;
    line-height: 47px;
  }
  .holder .holder-name { color: var(--ink-dark); }
  .holder .holder-role { color: var(--ink-light); }
  .contact-list {
    position: absolute;
    left: 0;
    top: 0;
    list-style: none;
    color: var(--ink-light);
    font-size: 40px;
    line-height: 1;
  }
  .contact-list li {
    position: absolute;
    white-space: nowrap;
  }
  .contact-phone { left: 624px; top: 352px; }
  .contact-email { left: 630px; top: 413px; }
  .contact-location { left: 630px; top: 477px; }
  .contact-web { left: 634px; top: 536px; }
</style>
</head>
<body>
<div class="canvas">
  <section class="card" aria-label="Brightwell Consulting business card">
    <svg class="card-shapes" viewBox="0 0 1072 628" aria-hidden="true">
      <polygon points="0,461 947,174 1072,352 1072,628 0,628" fill="var(--card-blue)"/>
      <!-- phone -->
      <path transform="translate(560,340) scale(2.25)" d="M6.62 10.79c1.44 2.83 3.76 5.14 6.59 6.59l2.2-2.2c.27-.27.67-.36 1.02-.24 1.12.37 2.33.57 3.57.57.55 0 1 .45 1 1V20c0 .55-.45 1-1 1-9.39 0-17-7.61-17-17 0-.55.45-1 1-1h3.5c.55 0 1 .45 1 1 0 1.25.2 2.45.57 3.57.11.35.03.74-.25 1.02l-2.2 2.2z" fill="var(--ink-dark)"/>
      <!-- envelope -->
      <rect x="566" y="412" width="52" height="36" fill="var(--ink-dark)"/>
      <g fill="none" stroke="var(--card-blue)" stroke-width="3">
        <polyline points="566,412 592,434 618,412"/>
        <line x1="566" y1="448" x2="585" y2="428"/>
        <line x1="618" y1="448" x2="599" y2="428"/>
      </g>
      <!-- location pin -->
      <path d="M591,462 c-14,0 -24,10 -24,23 c0,17 24,40 24,40 c0,0 24,-23 24,-40 c0,-13 -10,-23 -24,-23 z" fill="var(--ink-dark)"/>
      <circle cx="591" cy="483" r="8" fill="none" stroke="var(--card-blue)" stroke-width="4"/>
      <!-- globe -->
      <circle cx="591" cy="557" r="23" fill="var(--ink-dark)"/>
      <g fill="none" stroke="var(--card-blue)" stroke-width="2">
        <ellipse cx="591" cy="557" rx="10" ry="23"/>
        <line x1="591" y1="534" x2="591" y2="580"/>
        <line x1="568" y1="557" x2="614" y2="557"/>
        <line x1="572" y1="545" x2="610" y2="545"/>
        <line x1="572" y1="569" x2="610" y2="569"/>
      </g>
    </svg>

    <h1 class="brand-name">
      <span class="word-main">Brightwell</span>
      <span class="word-sub">CONSULTING</span>
    </h1>
    <p class="tagline">Inspiration to Dream More, Do More, Become More</p>

    <div class="holder">
      <p class="holder-name">EXAMPLE</p>
      <p class="holder-role">CEO/Manager</p>
    </div>

    <ul class="contact-list">
      <li class="contact-phone">123456789</li>
      <li class="contact-email">hi@brightwell.example</li>
      <li class="contact-location">Your location company</li>
      <li class="contact-web">www.yourcompany.com</li>
    </ul>
  </section>
</div>
</body>
</html>
```